Harbourline Green Jack Socials - Flyer

So now that i have the logo, I need a flyer made up for printing to be delivered to businesses and residential homes.
Below is some information that I want included in the design, in any order and in anyway.
What better way to spend time with family, friends or workmates then to enjoy 2 hours of barefoot bowls.
We can cater for Xmas Parties, Buck's and Hen's Parties, Birthday Parties, Team Building events.
We have food and drink packages to suit all your needs.
So why not come along and have the best fun you can have on 2 feet!
We have 2 locations at Wendlebrook Sports and Bowling Club and Mossvale Ridge Bowling Club
Prices start from $12pp for 2 hours of lawn bowls fun
Contact Colin Parrow on 0478 615 240 or visit our website www.greenjacksocials-example.com.au for more information and to enquire about your function today!

```html
<!DOCTYPE html>
<html lang="en">
<head>
<meta charset="utf-8">
<title>Harbourline Green Jack Socials – Flyer</title>
<link rel="stylesheet" href="https://fonts.googleapis.com/css2?family=Questrial&family=Arimo:wght@400;700&display=swap">
<style>
  :root {
    --teal: #22d6a2;
    --yellow: #f6d21c;
    --lime: #d2ea4e;
    --mint: #b4ecc6;
    --ink: #10231a;
    --cater-bg: rgba(92, 160, 66, 0.85);
    --price-bg: rgba(98, 104, 34, 0.9);
    --photo-border: #f4f4f0;
    --photo-venue-a: #9a86c4;
    --photo-venue-b: #6f8a72;
  }
  html, body { margin: 0; padding: 0; overflow: hidden; }
  body { width: 928px; height: 1200px; }
  .flyer {
    position: relative;
    width: 928px; height: 1200px; overflow: hidden;
    background: linear-gradient(180deg, #e8720c 0%, #a4520a 9%, #86640c 28%, #7a7c0e 48%, #7a6a0e 68%, #8e5a0c 86%, #dc6c10 100%);
    font-family: "Questrial", sans-serif;
  }
  .flyer > * { position: absolute; margin: 0; }

  .headline {
    left: 70px; top: 58px;
    color: var(--teal); font-size: 53px; line-height: 64px; font-weight: 400;
  }
  .headline strong { font-family: "Arimo", sans-serif; font-weight: 700; font-size: 50px; }

  .locations-title {
    left: 56px; top: 446px;
    color: var(--yellow); font-family: "Arimo", sans-serif; font-weight: 700; font-size: 29px; line-height: 36px;
  }

  .venue-label { text-align: center; color: var(--teal); }
  .venue-label b { display: block; font-family: "Arimo", sans-serif; font-weight: 700; }
  .venue-label span { display: block; }
  .venue-label--wendlebrook { left: 236px; top: 502px; width: 310px; }
  .venue-label--wendlebrook b { font-size: 32px; line-height: 38px; }
  .venue-label--wendlebrook span { font-size: 24px; line-height: 32px; }
  .venue-label--mossvale { left: 0; top: 545px; width: 252px; }
  .venue-label--mossvale b { font-size: 30px; line-height: 36px; }
  .venue-label--mossvale span { font-size: 28px; line-height: 40px; }

  .venue-photo { border: 1px solid var(--photo-border); box-sizing: border-box; }
  .venue-photo--wendlebrook {
    left: 250px; top: 577px; width: 292px; height: 220px;
    background: var(--photo-venue-a);
  }
  .venue-photo--mossvale {
    left: -1px; top: 622px; width: 296px; height: 222px;
    background: var(--photo-venue-b);
  }

  .packages { left: 616px; top: 396px; width: 300px; height: 210px; color: var(--yellow); }
  .packages span { position: absolute; white-space: nowrap; line-height: 1; }
  .packages .thin { font-weight: 400; }
  .packages .bold { font-family: "Arimo", sans-serif; font-weight: 700; }
  .packages .l1 { font-size: 57px; left: 0; top: 4px; }
  .packages .l2 { font-size: 31px; left: 3px; top: 55px; }
  .packages .l3 { font-size: 51px; left: 24px; top: 80px; }
  .packages .l4 { font-size: 44px; left: 3px; top: 128px; }
  .packages .l5 { font-size: 36px; left: 3px; top: 172px; }

  .cater {
    left: 557px; top: 662px; width: 371px; height: 180px;
    background: var(--cater-bg); box-sizing: border-box; padding: 4px 14px;
  }
  .cater h2 {
    margin: 0; color: var(--lime); line-height: 34px;
    font-family: "Arimo", sans-serif; font-weight: 700; font-size: 27px;
  }
  .cater ul { margin: 0; padding: 0; list-style: none; color: var(--mint); font-size: 27px; line-height: 35px; white-space: nowrap; }
  .cater li::before { content: "• "; }

  .invite {
    left: 431px; top: 912px; width: 480px; text-align: center; white-space: nowrap;
    color: var(--teal); font-family: "Arimo", sans-serif; font-weight: 700; font-size: 36px; line-height: 45px;
  }

  .price {
    left: 32px; top: 1008px; width: 376px; height: 77px;
    background: var(--price-bg); box-sizing: border-box; text-align: center; white-space: nowrap;
  }
  .price p { margin: 0; }
  .price .from { color: var(--yellow); font-size: 34px; line-height: 40px; margin-top: 2px; }
  .price .from b { font-family: "Arimo", sans-serif; font-weight: 700; }
  .price .detail { color: var(--yellow); font-family: "Arimo", sans-serif; font-weight: 700; font-size: 25px; line-height: 30px; }

  .contact-bar {
    left: 56px; top: 1105px; width: 872px; height: 82px;
    background: var(--teal); color: var(--ink);
  }
  .contact-bar .web { position: absolute; left: 16px; top: 14px; font-size: 29px; line-height: 28px; white-space: nowrap; }
  .contact-bar .web b { display: block; font-family: "Arimo", sans-serif; font-weight: 700; font-size: 27px; margin-left: 26px; }
  .contact-bar .divider { position: absolute; left: 574px; top: 10px; width: 2px; height: 62px; background: var(--ink); }
  .contact-bar .person { position: absolute; left: 604px; top: 14px; font-size: 29px; line-height: 28px; white-space: nowrap; }
  .contact-bar .person b { display: block; font-family: "Arimo", sans-serif; font-weight: 700; font-size: 28px; }
</style>
</head>
<body>
<main class="flyer">
  <h1 class="headline">What better way<br>to spend time with<br>family, friends or workmates<br>then to enjoy<br><strong>2 hours of barefoot bowls</strong>?</h1>

  <p class="locations-title">We have two locations:</p>

  <div class="venue-label venue-label--wendlebrook"><b>Wendlebrook</b><span>Sports and Bowling Club</span></div>
  <div class="venue-photo venue-photo--wendlebrook" role="img" aria-label="Photo of the Wendlebrook Sports and Bowling Club building"></div>

  <div class="venue-label venue-label--mossvale"><b>Mossvale Ridge</b><span>Bowling Club</span></div>
  <div class="venue-photo venue-photo--mossvale" role="img" aria-label="Photo of the Mossvale Ridge Bowling Club green"></div>

  <p class="packages">
    <span class="thin l1">We have</span>
    <span class="bold l2">food and drink</span>
    <span class="thin l3">packages</span>
    <span class="bold l4">to suit</span>
    <span class="bold l5">all your needs!</span>
  </p>

  <section class="cater">
    <h2>We can cater for:</h2>
    <ul>
      <li>Xmas Parties</li>
      <li>Buck's and Hen's Parties</li>
      <li>Birthday Parties</li>
      <li>Team Building events</li>
    </ul>
  </section>

  <p class="invite">So why not come along<br>and have the best fun<br>you can have on 2 feet!</p>

  <div class="price">
    <p class="from">Prices start from <b>$12pp</b></p>
    <p class="detail">for 2 hours of lawn bowls fun</p>
  </div>

  <footer class="contact-bar">
    <div class="web">visit our website for more information<b>www.greenjacksocials-example.com.au</b></div>
    <div class="divider"></div>
    <div class="person">Colin Parrow<b>0478 615 240</b></div>
  </footer>
</main>
</body>
</html>
```